Belmorin InsurTech Website Redesign - 10 Pages

Design a modern, professional website for Belmorin, an AI-native cyber insurance platform serving SMBs.

DELIVERABLE: 10 pages (desktop + mobile mockups)
- Homepage (priority #1)
- 4 Platform pages (Cyber Insurance, Brokers, Underwriters, Policyholder)
- 3 Company pages (About Us, Team, Contact/Careers)
- 2 Risk pages (AI Risk, Cyber Risk)

DESIGN DIRECTION:
- Professional + innovative (insurance meets technology)
- Trust-building + modern aesthetic
- Reference: Pellbrook Insurance, Driftmoor Insurance
- Use official brand colors (6-color palette provided)
- Avoid generic security clipart (padlocks, shields, magnifying glasses)
- Custom graphics, not AI-generated or stock imagery

CURRENT SITES FOR REFERENCE:
- www.belmorin-cover.test
- https://a3c9140d.belmorin-website.previewhost.test/

Full detailed brief with all content, page specifications, and brand guidelines attached as PDF (Belmorin_MockupLane_Brief.pdf).

TARGET AUDIENCE: Insurance brokers (primary), SMB business owners (secondary)
KEY MESSAGE: "Cyber Insurance the Way It Should Be"

Additional brand assets available in Google Drive - link provided on request.

```html
<!DOCTYPE html>
<html lang="en">
<head>
<meta charset="utf-8">
<title>Belmorin — Cyber Insurance the Way It Should Be</title>
<link href="https://fonts.googleapis.com/css2?family=Ubuntu:wght@400;500&family=Lato:wght@400;700&display=swap" rel="stylesheet">
<style>
:root{
  --brand:#3a2fe0;
  --brand-deep:#2a24b8;
  --navy:#1b2b6b;
  --ink:#4a4f66;
  --teal:#5fd3c9;
  --mint:#e6fbe9;
  --footer-a:#3db2ad;
  --footer-b:#6fd3cf;
  --band:#3a2cf0;
  --white:#ffffff;
}
*{box-sizing:border-box;margin:0;padding:0}
html,body{width:1200px;height:3117px;overflow:hidden;background:var(--white)}
body{position:relative;font-family:"Lato",sans-serif;color:var(--ink)}
.abs{position:absolute}
.heading{font-family:"Ubuntu",sans-serif;font-weight:500;color:var(--brand);text-align:center;font-size:33px;letter-spacing:.5px;width:1200px;left:0}

/* header */
.site-header{top:0;left:0;width:1200px;height:166px;background:#fff}
.nav-panel{left:300px;top:0;width:900px;height:122px;background:#fff;box-shadow:0 8px 10px rgba(0,0,0,.18);clip-path:polygon(0 0,100% 0,100% 100%,55px 100%)}
.brand-mark{left:206px;top:50px;display:flex;align-items:center;gap:8px;font-family:"Ubuntu",sans-serif;font-weight:500;font-size:26px;color:var(--brand)}
.brand-mark .dot{width:16px;height:16px;border-radius:50%;background:var(--brand)}
.nav-item{top:42px;font-family:"Ubuntu",sans-serif;font-size:19px;color:#222}
.nav-item.active{color:var(--brand);border-bottom:2px solid var(--brand);padding-bottom:2px}
.nav-item svg{vertical-align:middle;margin-left:3px}

/* hero */
.hero{top:166px;left:0;width:1200px;height:708px;background:radial-gradient(ellipse at 50% 45%,#6aa8e8 0%,#3a5fc4 30%,#2a2f9c 60%,#1d1f6e 100%)}
.hero-title{top:540px;left:0;width:1200px;text-align:center;font-family:"Ubuntu",sans-serif;font-weight:500;font-size:40px;color:#fff}
.hero-sub{top:606px;left:0;width:1200px;text-align:center;font-size:19px;color:#fff}
.hero-cta{top:709px;left:518px;width:166px;height:61px;background:#fff;border-radius:4px;font-family:"Ubuntu",sans-serif;font-weight:500;font-size:23px;color:var(--brand);display:flex;align-items:center;justify-content:center}

/* differentiators */
.mint-shape{left:820px;top:1240px;width:380px;height:1040px;background:var(--mint);clip-path:polygon(60% 0,100% 0,100% 100%,70% 90%,95% 60%,0 10%)}
.card{width:262px;height:532px;border:1.5px solid var(--brand);border-radius:4px;background:#fff;padding:8px}
.card.raised{border:none;box-shadow:0 6px 18px rgba(60,50,220,.28);height:512px}
.card-media{width:246px;height:192px;border-radius:2px}
.card-title{margin-top:24px;text-align:center;font-family:"Ubuntu",sans-serif;font-size:13px;line-height:22px;color:var(--brand-deep);padding:0 24px}
.card-copy{margin-top:12px;text-align:center;font-size:10.5px;line-height:18px;color:#555;padding:0 12px}
.card-copy p+p{margin-top:8px}
.card-btn{display:block;width:82px;height:28px;margin:18px auto 0;background:var(--teal);border-radius:4px;color:#fff;font-size:11px;font-weight:700;text-align:center;line-height:28px}
.carousel-arrow{top:1286px}

/* lifecycle */
.stage-title{font-family:"Ubuntu",sans-serif;font-size:19px;color:var(--navy);letter-spacing:.5px}
.stage-copy{font-size:15.5px;line-height:22.5px;color:#555;letter-spacing:.3px;width:215px}
.lifecycle-art{left:401px;top:1720px;width:400px;height:440px;border-radius:50% 50% 46% 46%;background:radial-gradient(circle at 50% 42%,#fff3c4 0%,#e8d58a 10%,#7fd8df 18%,#4a6178 30%,#56697f 44%,#e9f4f6 58%,#ffffff 72%)}

/* integrations */
.integration{top:2390px;width:200px;text-align:center}
.integration h3{margin-top:14px;font-family:"Ubuntu",sans-serif;font-weight:500;font-size:19px;color:var(--navy)}
.integration p{margin-top:10px;font-size:15.5px;line-height:22.5px;color:#555}

/* footer */
.site-footer{top:2623px;left:0;width:1200px;height:442px;background:linear-gradient(100deg,var(--footer-a),var(--footer-b) 55%,#4ec3c4)}
.footer-skyline{left:820px;top:2650px;width:380px;height:415px;background:linear-gradient(180deg,rgba(255,255,255,0) 0%,rgba(40,150,160,.45) 100%)}
.footer-brand{left:190px;top:2768px;display:flex;align-items:center;gap:8px;font-family:"Ubuntu",sans-serif;font-weight:500;font-size:27px;color:var(--brand)}
.footer-brand .dot{width:16px;height:16px;border-radius:50%;background:var(--brand)}
.footer-tag{left:184px;top:2832px;width:230px;font-size:12.5px;line-height:27px;color:#fff}
.footer-col{font-size:14px;line-height:27px;color:#fff}
.footer-col li{list-style:none}
.footer-col li:first-child{font-weight:700}
.bottom-band{top:3065px;left:0;width:1200px;height:52px;background:var(--band)}
</style>
</head>
<body>

<header class="abs site-header">
  <div class="abs nav-panel"></div>
  <div class="abs brand-mark"><span class="dot"></span>belmorin</div>
  <a class="abs nav-item active" style="left:379px">Home</a>
  <a class="abs nav-item" style="left:501px">Platform<svg width="12" height="8"><path d="M1 1l5 5 5-5" stroke="#222" stroke-width="2" fill="none"/></svg></a>
  <a class="abs nav-item" style="left:643px">Cyber Risk</a>
  <a class="abs nav-item" style="left:805px">AI Risk</a>
  <a class="abs nav-item" style="left:932px">Company<svg width="12" height="8"><path d="M1 1l5 5 5-5" stroke="#222" stroke-width="2" fill="none"/></svg></a>
</header>

<section class="abs hero" role="img" aria-label="Glowing crystal funnel distilling cyber security symbols over a digital city"></section>
<h1 class="abs hero-title">Cyber&nbsp; Insurance the Way It Should Be</h1>
<p class="abs hero-sub">Evidence based, automation driven underwriting&nbsp; for the AI era</p>
<a class="abs hero-cta">Contact Us</a>

<div class="abs mint-shape"></div>

<h2 class="abs heading" style="top:944px">What Makes Belmorin&nbsp; Different</h2>

<svg class="abs carousel-arrow" style="left:146px" width="16" height="24"><path d="M13 2L3 12l10 10" stroke="#999" stroke-width="2.5" fill="none"/></svg>
<svg class="abs carousel-arrow" style="left:1036px" width="16" height="24"><path d="M3 2l10 10L3 22" stroke="#999" stroke-width="2.5" fill="none"/></svg>

<article class="abs card" style="left:184px;top:1022px">
  <div class="card-media" role="img" aria-label="Printed analytics charts and reports on a desk" style="background:linear-gradient(135deg,#6b4a33,#e9eef2 40%,#cfe3f1)"></div>
  <h3 class="card-title">End&nbsp; to End Cyber Risk and Insurance Platform</h3>
  <div class="card-copy">
    <p>“The Belmorin platform streamlines the entire policy lifecycle, incentivizes and empowers policyholders to actively reduce their risk, and elevates brokers as trusted advisors.”</p>
    <p>Platform-driven assessment Automated analysis of cyber risk data -Inside-out integrations and outside-in data sources- AI analysis for risk prediction&nbsp; - Continuous risk monitoring.</p>
  </div>
  <a class="card-btn">Contact Us</a>
</article>

<article class="abs card" style="left:468px;top:1022px">
  <div class="card-media" role="img" aria-label="Laptop showing a security dashboard" style="background:linear-gradient(160deg,#2c2f36,#8a8f98 45%,#c9ccd2)"></div>
  <h3 class="card-title">Proprietary Tools and Rapid Response</h3>
  <div class="card-copy">
    <p>"Advanced security tools and 24/7 incident response capabilities protect businesses before, during, and after cyber events."</p>
    <p>In-house ransomware and system restoration 24/7 claims hotline with expert cyber triage - US-only on-site and remote support - Mix of in-house and verified expert contractors Real-time incident tracking</p>
  </div>
  <a class="card-btn">Contact Us</a>
</article>

<article class="abs card raised" style="left:754px;top:1022px">
  <div class="card-media" role="img" aria-label="Monitor displaying area charts in front of bookshelves" style="background:linear-gradient(180deg,#5a3b2a 0%,#c7cde8 25%,#b6bde6 70%,#2a2a2a 100%)"></div>
  <h3 class="card-title">Insurance DNA and Tech Execution</h3>
  <div class="card-copy">
    <p>"Founded by a team with deep expertise in cyber insurance and cybersecurity, we understand both the risk landscape and the insurance market."</p>
    <p>20+ years combined insurance experience Cybersecurity expertise from industry leaders - Former executives from Emberline, Corvane, Haldor XL - Built to address first-wave InsurTech short comings</p>
  </div>
  <a class="card-btn">Contact Us</a>
</article>

<h2 class="abs heading" style="top:1634px">The&nbsp; Complete&nbsp; Cyber&nbsp; Insurance&nbsp; Lifecycle</h2>

<div class="abs lifecycle-art" role="img" aria-label="Circular diagram of protection layers around a glowing core: predictive security, layered defense, policy compliance, supply chain resilience"></div>

<h3 class="abs stage-title" style="left:182px;top:1758px">ENSURE</h3>
<p class="abs stage-copy" style="left:184px;top:1791px">Best in class cyber insurance coverage with comprehensive first and third party protections</p>
<h3 class="abs stage-title" style="left:184px;top:1923px">ASSESS</h3>
<p class="abs stage-copy" style="left:184px;top:1957px">Dynamic scanning and read-only API integrations to continuously evaluate risk posture and inform underwriting</p>
<h3 class="abs stage-title" style="left:184px;top:2095px">IMPROVE</h3>
<p class="abs stage-copy" style="left:184px;top:2129px">Incentivize and guide policyholders to actively strengthen their cybersecurity through behavior rewards</p>
<h3 class="abs stage-title" style="left:823px;top:1758px">REMEDIATE</h3>
<p class="abs stage-copy" style="left:823px;top:1791px">Expert post-breach services including forensics, restoration, and crisis management support</p>
<h3 class="abs stage-title" style="left:823px;top:1924px">RENEW</h3>
<p class="abs stage-copy" style="left:823px;top:1957px">Seamless policy renewals with transparent pricing based on demonstrated risk improvements</p>

<h2 class="abs heading" style="top:2314px">Seamlessly Integrates With Your Tech Stack</h2>

<div class="abs integration" style="left:178px">
  <svg width="36" height="38" viewBox="0 0 36 38" fill="none" stroke="var(--brand)" stroke-width="2"><rect x="4" y="3" width="18" height="26" rx="1"/><circle cx="13" cy="12" r="3.5"/><path d="M8 22c1-4 9-4 10 0"/><path d="M20 33h12a5 5 0 0 0-2-10 6 6 0 0 0-11 3 4 4 0 0 0 1 7z"/></svg>
  <h3>Identity Platforms</h3>
  <p>Examples: Quillnet Workspace, Keystile, Cerulea ID</p>
</div>
<div class="abs integration" style="left:390px">
  <svg width="36" height="38" viewBox="0 0 36 38" fill="none" stroke="var(--brand)" stroke-width="2"><path d="M18 2l15 9v16l-15 9-15-9V11z"/><path d="M9 15l9 5 9-5M9 20l9 5 9-5M9 25l9 5 9-5"/></svg>
  <h3>Developer Platforms</h3>
  <p>Examples: CodeHarbor, RepoMill</p>
</div>
<div class="abs integration" style="left:608px">
  <svg width="40" height="38" viewBox="0 0 40 38" fill="none" stroke="var(--brand)" stroke-width="2"><path d="M20 2l9 4v7c0 6-4 9-9 11-5-2-9-5-9-11V6z"/><circle cx="20" cy="12" r="3"/><path d="M20 24v5M6 29h28M6 29v3M20 29v3M34 29v3"/><rect x="2" y="32" width="8" height="4"/><rect x="16" y="32" width="8" height="4"/><rect x="30" y="32" width="8" height="4"/></svg>
  <h3>Endpoint Security</h3>
  <p>Examples: Ravenguard, Northwall Defender, Vantor XDR</p>
</div>
<div class="abs integration" style="left:820px">
  <svg width="40" height="38" viewBox="0 0 40 38" fill="none" stroke="var(--brand)" stroke-width="2"><path d="M10 16a8 8 0 0 1 15-6 7 7 0 0 1 11 6"/><rect x="4" y="16" width="14" height="6" rx="1"/><rect x="4" y="24" width="14" height="6" rx="1"/><rect x="22" y="20" width="12" height="14" rx="1"/><circle cx="28" cy="27" r="2"/></svg>
  <h3>Cloud Infrastructure</h3>
  <p>Examples: Skyloft, Cerulea Cloud, Quillnet Cloud</p>
</div>

<footer class="abs site-footer"></footer>
<div class="abs footer-skyline" role="img" aria-label="Faint digital city skyline"></div>
<div class="abs footer-brand"><span class="dot"></span>belmorin</div>
<p class="abs footer-tag">Reducing the frequency and severity of cyber risk by strengthening organizations' cyber risk posture.</p>
<ul class="abs footer-col" style="left:468px;top:2828px"><li>Home</li><li>Platform</li><li>Cyber Risk</li><li>AI Risk</li><li>Company</li></ul>
<ul class="abs footer-col" style="left:658px;top:2830px"><li>Company</li><li>The Problem</li><li>The Solution</li><li>How it Works</li></ul>
<ul class="abs footer-col" style="left:825px;top:2830px"><li>Other</li><li>Privacy Policy</li><li>Terms and Conditions</li></ul>
<div class="abs bottom-band"></div>

</body>
</html>
```